依頼詳細
PCとスマホデザインの両方納品をいただきますが、
まずはデザインイメージが確認しやすいPCページのみの提案をお願いします。
スマホページは当選者に納品時にお願いしたいと思います。
スマホサイズは横幅750pxのサイズで作成してください。
(Lumexaディスプレイに対応するため)
レスポンシブウェブデザインを意識したデザインでお願いします。

■サイトマップ
添付の画面遷移図をご確認ください。

■参考サイト
https://kelparoute.com/
https://mivolune.jp/sportsevent/

■内容について
建築工務店が開催するイベント情報を掲載・告知をするサイトになります。
開催するイベント内容は添付のチラシのような内容の予定です。

■素材写真
画像データについては、フリー素材から流用して
イメージ画像に当て込んでください。
足りない場合は、一旦他のサイトの写真をサンプルとして
入れてください。(サンプルなどの表記をお願いします)
また、購入が必要な写真などを利用した場合、
価格とサイト名を教えてください。

また、Velmora Stockで定期契約をしていますので、
Velmora Stockの画像は使用できます。
デザイン時はカンプ画像をお入れいただきますようお願いします。

■ワイヤーフレーム
https://wire.pelvrin.com/view/a7392cdd-1148-4f0b-9d3e-e84521b07f3a-d318/
コンテンツの構成としてワイヤーフレームを作成しましたが
必ずしもワイヤーフレームの通りではなくて大丈夫です。
TOPページに配置するコンテンツを見ていただき、デザインは
デザイナーの皆様におまかせしたいと思います。

----------------------------------------------------------------------------
【制作物に対するお願い】

■サイズについて
TOPデザイン自体のアートボードサイズは、
横幅1366px、コンテンツ幅は1000pxでお願いします。
(縦幅の制限はございません)

■フォントについて
・無料で使えるフォントで作成をお願いします。
・OSに紐づくフォントの使用は控えていただければと思います (ヒラギノなど)

サイトURL
ページ数
1ページ
希望イメージ
シンプル 複雑
単色 カラフル
暗い 明るい
日常 高級
遊び心 厳粛
未来的 伝統的
女性的 男性的
希望する色
ベースカラー:白、緑 ポイントカラー:オレンジ
納品ファイル
• イラストレーター形式 (.ai)
• フォトショップ形式 (.psd)
補足説明
上記のいずれか1つ(アウトラインありとなしの2つ)と高解像度JPGを納品お願いします。
ロゴデータを追加で添付しました。

```html
<!DOCTYPE html>
<html lang="ja">
<head>
<meta charset="utf-8">
<title>NOVAHAUS イベント</title>
<link href="https://fonts.googleapis.com/css2?family=Noto+Sans+JP:wght@400;500;700&family=Noto+Serif+JP:wght@500;700&display=swap" rel="stylesheet">
<style>
:root{
  --green:#13a538;
  --orange:#f26a3b;
  --ink:#333;
  --sub:#777;
  --line:#c9c9c9;
  --white:#fff;
  --wood:#b88a5e;
}
*{box-sizing:border-box;margin:0;padding:0}
html,body{width:1200px;height:2584px;overflow:hidden;background:var(--white);font-family:"Noto Sans JP",sans-serif;color:var(--ink)}
.page{position:relative;width:1200px;height:2584px}
.brand{position:absolute;left:32px;top:28px;display:flex;align-items:center;gap:10px}
.brand-mark{width:14px;height:14px;background:var(--ink)}
.brand-name{font-size:18px;font-weight:700;letter-spacing:2px}
.social{position:absolute;right:34px;top:26px;display:flex;gap:14px}
.social span{width:22px;height:22px;border-radius:50%;background:var(--green)}
.hero-photo{position:absolute;left:340px;top:96px;width:860px;height:470px;background:linear-gradient(120deg,#8a6a4c,#c79b6c 45%,#6e5646 80%,#4a3a32)}
.hero-box{position:absolute;left:190px;top:250px;width:440px;height:230px;background:var(--white);padding:28px 20px}
.hero-title{font-family:"Noto Serif JP",serif;font-size:54px;font-weight:500;letter-spacing:3px;line-height:1}
.hero-lead{margin-top:22px;font-size:12px;line-height:1.9}
.btn{display:inline-block;color:var(--white);font-size:13px;text-align:center}
.btn-green{background:var(--green)}
.btn-orange{background:var(--orange)}
.hero-btn{position:absolute;left:400px;top:412px;width:220px;height:46px;line-height:46px}
.heading{position:absolute;left:152px;font-size:20px;font-weight:700;color:var(--green);letter-spacing:2px}
.tag{position:absolute;top:700px;width:112px;height:24px;line-height:24px;font-size:10px}
.grid{position:absolute;left:152px;top:784px;width:888px;display:grid;grid-template-columns:repeat(3,284px);row-gap:40px;column-gap:18px}
.card{height:122px;border:1px solid #999;display:flex;padding:10px;gap:12px}
.card-photo{width:118px;height:74px;background:linear-gradient(135deg,#3b2b22,#8a5a36 60%,#2b211c)}
.card-title{font-size:11px;margin-bottom:8px}
.card-meta{font-size:9px;color:var(--sub);line-height:2}
.more{position:absolute;left:520px;width:160px;height:40px;line-height:40px;font-size:12px}
.news{position:absolute;left:152px;top:1480px;width:888px;list-style:none;border-top:2px dotted var(--line)}
.news li{height:80px;display:flex;align-items:center;border-bottom:2px dotted var(--line);font-size:12px;padding-left:10px}
.news time{width:190px}
.news p{flex:1;color:var(--sub)}
.news svg{margin-right:30px}
.map{position:absolute;left:220px;top:2016px;width:400px;height:272px;border:1px solid #999;background:#f3f3f0;display:flex;align-items:center;justify-content:center}
.info{position:absolute;left:726px;top:2016px;font-size:12px;line-height:1.8}
.info dt{color:var(--ink)}
.info dd{color:var(--sub);margin:0 0 12px 12px}
.form-note{position:absolute;left:0;width:1200px;top:2420px;text-align:center;font-size:12px;color:var(--sub)}
.form-btn{position:absolute;left:490px;top:2460px;width:220px;height:48px;line-height:48px}
.to-top{position:absolute;left:1150px;top:2476px;width:30px;height:30px;border:1px solid #999;background:var(--white);display:flex;align-items:center;justify-content:center}
.footer{position:absolute;left:0;top:2532px;width:1200px;height:52px;background:var(--green);color:var(--white);font-size:12px;text-align:center;line-height:52px}
</style>
</head>
<body>
<div class="page">
  <header>
    <div class="brand"><span class="brand-mark"></span><span class="brand-name">NOVAHAUS</span></div>
    <div class="social" aria-label="SNSリンク"><span></span><span></span><span></span></div>
  </header>

  <section class="hero">
    <div class="hero-photo" role="img" aria-label="木材に釘を打つ子どもの手元の写真"></div>
    <div class="hero-box">
      <h1 class="hero-title">NOVAHAUS</h1>
      <p class="hero-lead">この場所から、まちの新たな出会いが始まる　スタッフのさまざまな<br>体験を通じて地域の「暮らし」を育てていく</p>
    </div>
    <a class="btn btn-green hero-btn">お申込みはこちら　›</a>
  </section>

  <h2 class="heading" style="top:700px">最新イベント</h2>
  <span class="btn btn-green tag" style="left:640px">開催予定イベント</span>
  <span class="btn btn-orange tag" style="left:820px">過去のイベント</span>
  <div class="grid">
    <div class="card"><div class="card-photo" role="img" aria-label="イベント写真"></div><div><p class="card-title">【イベント名】</p><p class="card-meta">開催日　0000.00.00<br>場所　　会場名<br>料金　　0,000円</p></div></div>
    <div class="card"><div class="card-photo" role="img" aria-label="イベント写真"></div><div><p class="card-title">【イベント名】</p><p class="card-meta">開催日　0000.00.00<br>場所　　会場名<br>料金　　0,000円</p></div></div>
    <div class="card"><div class="card-photo" role="img" aria-label="イベント写真"></div><div><p class="card-title">【イベント名】</p><p class="card-meta">開催日　0000.00.00<br>場所　　会場名<br>料金　　0,000円</p></div></div>
    <div class="card"><div class="card-photo" role="img" aria-label="イベント写真"></div><div><p class="card-title">【イベント名】</p><p class="card-meta">開催日　0000.00.00<br>場所　　会場名<br>料金　　0,000円</p></div></div>
    <div class="card"><div class="card-photo" role="img" aria-label="イベント写真"></div><div><p class="card-title">【イベント名】</p><p class="card-meta">開催日　0000.00.00<br>場所　　会場名<br>料金　　0,000円</p></div></div>
    <div class="card"><div class="card-photo" role="img" aria-label="イベント写真"></div><div><p class="card-title">【イベント名】</p><p class="card-meta">開催日　0000.00.00<br>場所　　会場名<br>料金　　0,000円</p></div></div>
    <div class="card"><div class="card-photo" role="img" aria-label="イベント写真"></div><div><p class="card-title">【イベント名】</p><p class="card-meta">開催日　0000.00.00<br>場所　　会場名<br>料金　　0,000円</p></div></div>
    <div class="card"><div class="card-photo" role="img" aria-label="イベント写真"></div><div><p class="card-title">【イベント名】</p><p class="card-meta">開催日　0000.00.00<br>場所　　会場名<br>料金　　0,000円</p></div></div>
    <div class="card"><div class="card-photo" role="img" aria-label="イベント写真"></div><div><p class="card-title">【イベント名】</p><p class="card-meta">開催日　0000.00.00<br>場所　　会場名<br>料金　　0,000円</p></div></div>
  </div>
  <a class="btn btn-orange more" style="top:1288px">イベント情報一覧</a>

  <h2 class="heading" style="top:1392px">お知らせ</h2>
  <ul class="news">
    <li><time>2021.00.00</time><p>テキストが入ります。テキストが入ります。テキストが入ります。</p><svg width="10" height="18" viewBox="0 0 10 18"><path d="M1 1l8 8-8 8" fill="none" stroke="#999"/></svg></li>
    <li><time>2021.00.00</time><p>テキストが入ります。テキストが入ります。テキストが入ります。</p><svg width="10" height="18" viewBox="0 0 10 18"><path d="M1 1l8 8-8 8" fill="none" stroke="#999"/></svg></li>
    <li><time>2021.00.00</time><p>テキストが入ります。テキストが入ります。テキストが入ります。</p><svg width="10" height="18" viewBox="0 0 10 18"><path d="M1 1l8 8-8 8" fill="none" stroke="#999"/></svg></li>
    <li><time>2021.00.00</time><p>テキストが入ります。テキストが入ります。テキストが入ります。</p><svg width="10" height="18" viewBox="0 0 10 18"><path d="M1 1l8 8-8 8" fill="none" stroke="#999"/></svg></li>
  </ul>
  <a class="btn btn-orange more" style="top:1846px">お知らせ一覧</a>

  <h2 class="heading" style="top:1946px">アクセス</h2>
  <div class="map" role="img" aria-label="会場周辺の地図">
    <svg width="26" height="36" viewBox="0 0 26 36"><path d="M13 0C6 0 0 6 0 13c0 9 13 23 13 23s13-14 13-23C26 6 20 0 13 0z" fill="#333"/><circle cx="13" cy="13" r="5" fill="#f3f3f0"/></svg>
  </div>
  <dl class="info">
    <dt>会場</dt><dd>テキストが入ります</dd>
    <dt>住所</dt><dd>〒000-0000 ○○県○○市○○町0-0</dd>
    <dt>営業時間</dt><dd>00:00〜00:00</dd>
    <dt>定休日</dt><dd>00:00〜00:00</dd>
  </dl>

  <h2 class="heading" style="top:2346px">イベント申し込みフォーム</h2>
  <p class="form-note">イベントのお申し込みはこちらから受け付けております</p>
  <a class="btn btn-green form-btn">お申込みはこちら　›</a>
  <div class="to-top"><svg width="12" height="12" viewBox="0 0 12 12"><path d="M1 8l5-5 5 5" fill="none" stroke="#555"/></svg></div>

  <footer class="footer">copyright©</footer>
</div>
</body>
</html>
```